Uncle Bramble's Local Produce Delivery

Two-sided postcard.

Front side: Can be a photo of available products. Need at least a 2" x 4" space to speak to the recipient and let them know who the post card is for and who it is from.

Back side: We will apply a sticker for the delivery address and space should be included for stamp.

```html
<!DOCTYPE html>
<html lang="en">
<head>
<meta charset="utf-8">
<title>Uncle Bramble's Local Produce Delivery – Postcard</title>
<link href="https://fonts.googleapis.com/css2?family=Roboto:wght@400;500;700&display=swap" rel="stylesheet">
<style>
  :root {
    --bg: #d6d6d6;
    --cream: #fcfbef;
    --green: #1a803f;
    --green-dark: #137a0c;
    --yellow: #f3f520;
    --yellow-deep: #c9c91c;
    --ink: #555555;
    --label: #6b6b6b;
    --rule: #8c8c8c;
    --rule-light: #c8c8c8;
  }
  * { margin: 0; padding: 0; box-sizing: border-box; }
  html, body { width: 674px; height: 1200px; overflow: hidden; background: var(--bg); }
  body { position: relative; font-family: 'Roboto', Arial, sans-serif; }

  /* Front side */
  .front {
    position: absolute; left: 53px; top: 53px; width: 485px; height: 324px;
    background: linear-gradient(135deg, var(--green), var(--yellow) 50%, var(--green));
  }
  .front__inner {
    position: absolute; inset: 15px; background: var(--cream);
  }
  .front__heading {
    position: absolute; left: 22px; top: 34px;
    font-size: 14.5px; font-weight: 500; line-height: 18px; color: var(--ink);
  }
  .front__message {
    position: absolute; left: 22px; top: 80px; width: 240px;
    font-size: 7.1px; line-height: 9.1px; color: var(--ink);
  }
  .front__photo {
    position: absolute; left: 41px; top: 137px; width: 171px; height: 133px;
    border-radius: 40px 40px 30px 30px;
    background: radial-gradient(ellipse at 65% 45%, #c98a5c 0%, #d9b48c 40%, #f2efe6 75%, var(--cream) 100%);
  }
  .front__divider {
    position: absolute; left: 276px; top: 24px; width: 1px; height: 248px; background: var(--rule-light);
  }
  .brand-seal {
    position: absolute; left: 339px; top: 21px; width: 96px; height: 96px; border-radius: 50%;
    background: var(--yellow);
    display: flex; align-items: center; justify-content: center; text-align: center;
  }
  .brand-seal__name {
    font-size: 13px; font-weight: 700; line-height: 15px; color: var(--green-dark);
  }
  .from-label {
    position: absolute; left: 291px; top: 182px; font-size: 13px; font-weight: 500; color: var(--ink);
  }
  .rule { position: absolute; height: 1px; background: var(--rule-light); }

  /* Back side – delivery sticker */
  .sticker {
    position: absolute; left: 147px; width: 485px; height: 323px; overflow: hidden;
    border: 6px solid var(--green); background: var(--cream);
  }
  .sticker--light { top: 415px; }
  .sticker--dark { top: 774px; border-color: var(--yellow); background: var(--green); }

  .sticker__tab {
    position: absolute; left: 135px; top: 0; width: 202px; height: 30px;
    clip-path: polygon(0 0, 100% 0, 95.5% 100%, 4.5% 100%);
    background: var(--green);
    display: flex; align-items: center; justify-content: center;
    font-size: 15.5px; font-weight: 700; color: var(--yellow); letter-spacing: 0.2px;
  }
  .sticker--dark .sticker__tab { background: var(--yellow); color: var(--green); }

  .field-label {
    position: absolute; font-size: 10.5px; font-weight: 500; color: var(--label); line-height: 12px;
  }
  .sticker--dark .field-label { color: var(--yellow); }
  .field-line { position: absolute; height: 1px; background: var(--rule); }
  .sticker--dark .field-line { background: #ffffff; }

  .sticker__ghost {
    position: absolute; left: 328px; top: 168px; width: 144px; height: 144px; border-radius: 50%;
    background: rgba(0,0,0,0.025);
  }
  .stamp-box {
    position: absolute; left: 354px; top: 200px; width: 94px; height: 94px; border-radius: 50%;
    background: var(--yellow); border: 5px solid var(--green-dark);
    display: flex; align-items: center; justify-content: center;
  }
  .sticker--dark .stamp-box { border-color: var(--yellow-deep); }
  .stamp-box__inner {
    width: 64px; height: 64px; border-radius: 50%; border: 2px solid var(--green-dark);
    display: flex; align-items: center; justify-content: center;
    font-size: 13px; font-weight: 500; color: var(--green-dark);
  }
</style>
</head>
<body>

<section class="front" role="img" aria-label="green and yellow airmail stripe border">
  <div class="front__inner">
    <h1 class="front__heading">AT VEOEOS<br>ETACCUSAMUS</h1>
    <p class="front__message">At vero eos et accusamus et iusto odidignissimos ducimuqui blandit iis lop raesentium voluptatum deleniti atque corrupti quos dolores et quas molesti exceptur.At vero eos et accusamus et iusto oddigniss imos ducimuqui bladitiis p raesentium voluptatum delenti atque co rrupti quos dolores etuas molestis exceptur.</p>
    <div class="front__photo" role="img" aria-label="Photo of fresh milk in a bottle and glass beside a wooden bowl of brown eggs"></div>
    <div class="front__divider"></div>
    <div class="brand-seal"><span class="brand-seal__name">Uncle<br>Bramble's</span></div>
    <span class="from-label">FROM</span>
    <div class="rule" style="left:338px;top:192px;width:97px"></div>
    <div class="rule" style="left:292px;top:211px;width:143px"></div>
    <div class="rule" style="left:292px;top:227px;width:143px"></div>
    <div class="rule" style="left:292px;top:244px;width:143px"></div>
    <div class="rule" style="left:292px;top:260px;width:143px"></div>
  </div>
</section>

<section class="sticker sticker--light">
  <div class="sticker__ghost"></div>
  <div class="sticker__tab">DELIVERY ADDRESS</div>
  <span class="field-label" style="left:356px;top:14px">Date:</span>
  <div class="field-line" style="left:383px;top:22px;width:57px"></div>
  <span class="field-label" style="left:31px;top:62px">Name:</span>
  <div class="field-line" style="left:68px;top:70px;width:373px"></div>
  <span class="field-label" style="left:31px;top:86px">Product Name:</span>
  <div class="field-line" style="left:108px;top:94px;width:333px"></div>
  <span class="field-label" style="left:31px;top:110px">Dispatch Amount:</span>
  <div class="field-line" style="left:126px;top:118px;width:315px"></div>
  <div class="field-line" style="left:31px;top:143px;width:410px"></div>
  <span class="field-label" style="left:31px;top:159px">Mobile Number:</span>
  <div class="field-line" style="left:114px;top:168px;width:327px"></div>
  <span class="field-label" style="left:31px;top:186px">Address:</span>
  <div class="field-line" style="left:78px;top:194px;width:267px"></div>
  <div class="field-line" style="left:32px;top:222px;width:311px"></div>
  <div class="field-line" style="left:32px;top:249px;width:311px"></div>
  <div class="field-line" style="left:32px;top:279px;width:311px"></div>
  <div class="stamp-box"><div class="stamp-box__inner">STAMP</div></div>
</section>

<section class="sticker sticker--dark">
  <div class="sticker__tab">DELIVERY ADDRESS</div>
  <span class="field-label" style="left:356px;top:14px">Date:</span>
  <div class="field-line" style="left:383px;top:22px;width:57px"></div>
  <span class="field-label" style="left:31px;top:62px">Name:</span>
  <div class="field-line" style="left:68px;top:70px;width:373px"></div>
  <span class="field-label" style="left:31px;top:86px">Product Name:</span>
  <div class="field-line" style="left:108px;top:94px;width:333px"></div>
  <span class="field-label" style="left:31px;top:110px">Dispatch Amount:</span>
  <div class="field-line" style="left:126px;top:118px;width:315px"></div>
  <div class="field-line" style="left:31px;top:143px;width:410px"></div>
  <span class="field-label" style="left:31px;top:159px">Mobile Number:</span>
  <div class="field-line" style="left:114px;top:168px;width:327px"></div>
  <span class="field-label" style="left:31px;top:186px">Address:</span>
  <div class="field-line" style="left:78px;top:194px;width:267px"></div>
  <div class="field-line" style="left:32px;top:222px;width:311px"></div>
  <div class="field-line" style="left:32px;top:249px;width:311px"></div>
  <div class="field-line" style="left:32px;top:279px;width:311px"></div>
  <div class="stamp-box"><div class="stamp-box__inner">STAMP</div></div>
</section>

</body>
</html>
```